Up and coming mattress store needs a better website design

We are a family owned mattress store called QR Bedding and we are in need of a better looking website. We have started advertising online and our current website qrbeddingshop.com is really bad. We are looking for at lest 4 pages including: welcome page, about us page, our mattresses page, and contact us page. Here is a wire frame of something I was thinking of https://mockboard.example/7kq2ZP it doesn't have to be like this it is just an idea. Some must haves are: Name, Logo, at lest 3 spots for links for financing, a bigger spot for special offers, maybe the number and address for the store at the very bottom. You can submit a one page welcome design to start with and if I like it we can move on from there. Thank you for your time!

Target Market(s)

20 to 40 year olds who want to buy mattresses

Industry/Entity Type

Store

Coding

Coded - Design and coding required

Number of Pages Required

4 page

Requirements
Must have
• name, logo, 3 spots for links for our no credit check financing companies
Nice to have
• All stores addresses and numbers at the bottom: Main Store 4870 Marlow Ave Brookfield 60513 (346)-555-0182 Smaller Store 915 Cedar Loop Linden Tx 75563 (281)-555-0139

```html
<!DOCTYPE html>
<html lang="en">
<head>
<meta charset="utf-8">
<title>QR Bedding – Welcome</title>
<link rel="stylesheet" href="https://fonts.googleapis.com/css2?family=Open+Sans:wght@400;600;700;800&display=swap">
<style>
:root{
  --red:#b5121b;
  --red-dark:#8c0d14;
  --ink:#222;
  --footer:#232323;
  --footer-deep:#161616;
  --paper:#fff;
  --muted:#9a9a9a;
}
*{box-sizing:border-box;margin:0;padding:0}
html,body{width:736px;height:1200px;overflow:hidden;background:var(--paper);font-family:"Open Sans",Arial,sans-serif;color:var(--ink)}
.page{position:relative;width:736px;height:1200px}

/* top bar */
.topbar{height:24px;background:var(--red-dark);display:flex;align-items:center;justify-content:space-between;padding:0 98px;font-size:8px;color:#f3d6d6}
.topbar .contact-line{display:flex;gap:14px}
.topbar .contact-line span{display:flex;align-items:center;gap:4px}
.topbar svg{width:9px;height:9px;fill:#f3d6d6}

/* hero */
.hero{position:relative;height:332px}
.hero-photo{position:absolute;inset:0;background:radial-gradient(ellipse at 40% 60%,#d9c9b4 0%,#a88a66 35%,#5e4632 70%,#33261c 100%)}
.nav{position:absolute;top:0;left:0;right:0;height:46px;background:rgba(20,14,12,.72);display:flex;align-items:center;justify-content:space-between;padding:0 98px}
.brand{display:flex;align-items:center;gap:7px;font-weight:800;font-size:17px;color:var(--red)}
.brand .mark{width:20px;height:20px;background:var(--red)}
.nav ul{list-style:none;display:flex;gap:22px;font-size:10px;font-weight:600}
.nav a{color:#fff;text-decoration:none;padding-bottom:4px}
.nav a.active{border-bottom:2px solid var(--red)}
.hero-copy{position:absolute;top:146px;left:300px;width:236px;text-align:center;color:#fff}
.hero-copy h1{font-size:21px;font-weight:700;letter-spacing:.3px}
.hero-copy p{font-size:9px;margin-top:3px;line-height:1.35}
.btn{display:inline-block;background:var(--red);color:#fff;font-size:9px;font-weight:700;padding:6px 12px;text-decoration:none;letter-spacing:.5px}
.hero-copy .btn{margin-top:12px}

/* feature grid */
.features{display:grid;grid-template-columns:98px 184px 172px 184px 98px;grid-template-rows:117px 117px}
.photo{background:linear-gradient(135deg,#cfc7bf,#8b7d70)}
.photo.warm{background:linear-gradient(135deg,#e7ddd0,#9c7a5c)}
.photo.dark{background:linear-gradient(135deg,#6d5a4d,#2e241e)}
.photo.white{background:linear-gradient(135deg,#f4f1ee,#bdb4ab)}
.tile-red{background:var(--red);color:#fff;padding:12px 14px;text-align:center}
.tile-red h2{font-size:13px;font-weight:700;margin-bottom:6px}
.tile-red p{font-size:7px;line-height:1.45}
.tile-red.plain{padding-top:26px}

/* intro */
.intro{width:540px;margin:14px auto 0;text-align:center;font-size:8.5px;line-height:1.55}
.intro strong{font-weight:700}

/* finance partners */
.partners{display:flex;justify-content:center;gap:24px;margin-top:38px}
.partner{width:136px;height:52px;background:#fff;box-shadow:0 1px 4px rgba(0,0,0,.25);display:flex;align-items:center;justify-content:center;gap:6px;font-size:11px;font-weight:700;color:var(--red-dark)}
.partner .dot{width:12px;height:12px;background:var(--red-dark)}

/* offer */
.offer{display:flex;width:540px;height:189px;margin:28px auto 0}
.offer-photo{flex:0 0 338px;background:linear-gradient(135deg,#eeeae6,#a49b92)}
.offer-box{flex:1;background:var(--red);color:#fff;text-align:center;padding:26px 14px;font-size:12.5px;line-height:1.4}
.offer-box .btn{background:#1a1a1a;margin-top:10px;padding:5px 11px;font-size:8px}

/* footer */
.site-footer{position:absolute;left:0;right:0;top:980px;height:198px;background:var(--footer);color:#ddd;display:flex;padding:20px 98px 0}
.site-footer h3{font-size:12px;font-weight:600;color:#fff;margin-bottom:12px}
.links{width:118px}
.links ul{list-style:none;font-size:8px;line-height:1.9}
.links a{color:#ddd;text-decoration:none}
.quick-contact{width:170px}
.field{width:120px;height:15px;background:#fff;margin-bottom:5px;font-size:7px;color:var(--muted);padding:3px 5px;display:block}
.field.message{height:30px}
.submit{background:var(--red);color:#fff;font-size:8px;font-weight:700;padding:4px 10px;display:inline-block}
.map{width:130px;height:130px;border-radius:50%;background:radial-gradient(circle at 45% 45%,#f2efe6,#d7d9c9 55%,#b8c7d6);margin-top:4px;border:4px solid #fff}
.follow{margin-left:26px}
.follow ul{list-style:none;font-size:7px}
.follow li{display:flex;align-items:center;gap:6px;margin-bottom:8px}
.follow .circle{width:16px;height:16px;border-radius:50%}
.c1{background:#3b5a98}.c2{background:#2aa9e0}.c3{background:#1d77b5}.c4{background:#d9452f}
.copyright{position:absolute;left:0;right:0;bottom:0;height:22px;background:var(--footer-deep);color:#888;font-size:7px;display:flex;align-items:center;justify-content:center}
</style>
</head>
<body>
<div class="page">
  <div class="topbar">
    <span>We are a family owned &amp; operated mattress store</span>
    <div class="contact-line">
      <span><svg viewBox="0 0 10 10"><path d="M0 2h10v6H0z M0 2l5 3 5-3" fill="none" stroke="#f3d6d6"/></svg>hello@qrbeddingshop.com</span>
      <span><svg viewBox="0 0 10 10"><path d="M2 0l2 2-1 2c1 1 2 2 3 3l2-1 2 2-2 2C4 10 0 6 0 2z"/></svg>(346)-555-0182</span>
    </div>
  </div>

  <header class="hero">
    <div class="hero-photo" role="img" aria-label="Ornate bedroom with a carved gold and pink upholstered bed"></div>
    <nav class="nav">
      <div class="brand"><span class="mark"></span>QR Bedding</div>
      <ul>
        <li><a class="active" href="#">Home</a></li>
        <li><a href="#">About Us</a></li>
        <li><a href="#">Our Mattresses</a></li>
        <li><a href="#">Contact Us</a></li>
      </ul>
    </nav>
    <div class="hero-copy">
      <h1>Brand Bed BOX 50%</h1>
      <p>Brand New Mattresses, Box Springs &amp; Beds At Great Low Prices</p>
      <a class="btn" href="#">BUY NOW</a>
    </div>
  </header>

  <section class="features">
    <div class="photo warm" role="img" aria-label="Bedroom lamp and headboard"></div>
    <div class="tile-red">
      <h2>About QR Bedding</h2>
      <p>Only The Best Quality Mattress Here At QR Bedding. Family Owned And Run, We Treat Every Guest Like Family. Come See Us Today For Great Deals.</p>
    </div>
    <div class="photo dark" role="img" aria-label="Modern bedroom with a made bed"></div>
    <div class="tile-red">
      <h2>Contact Us</h2>
      <p>Main Store<br>4870 Marlow Ave Brookfield 60513<br>(346)-555-0182<br><br>Smaller Store<br>915 Cedar Loop Linden Tx 75563<br>(281)-555-0139</p>
    </div>
    <div class="photo" role="img" aria-label="Mattress corner detail"></div>

    <div class="photo white" role="img" aria-label="Stacked mattresses"></div>
    <div class="photo white" role="img" aria-label="Stacked mattresses in the showroom"></div>
    <div class="tile-red plain">
      <p>Save Big Every Day With No Credit Check Financing. Only $40 Down To Take Home A New Mattress Today And Pay Later.</p>
    </div>
    <div class="photo dark" role="img" aria-label="Bed with dark frame"></div>
    <div class="photo warm" role="img" aria-label="Mattress close-up"></div>
  </section>

  <p class="intro"><strong>Lorem ipsum dolor sit amet, consectetur adipiscing elit. Sed vel lacus vehicula, aliquam urna non, molestie lectus.</strong> Vivamus finibus pellentesque nisi ac ullamcorper. Morbi aliquam mauris sit amet mi mattis fringilla.</p>

  <div class="partners">
    <div class="partner"><span class="dot"></span>Ledgerline Funding</div>
    <div class="partner">Stepwise Lease</div>
    <div class="partner">Summit Credit</div>
  </div>

  <section class="offer">
    <div class="offer-photo" role="img" aria-label="White bedding with pillows on a bed"></div>
    <div class="offer-box">
      We Use Ledgerline Funding, Stepwise Lease, Summit Credit. It Needs To Say 40 Dollars Down No Credit Check 90 Days Same As Cash
      <br><a class="btn" href="#">VIEW NOW</a>
    </div>
  </section>

  <footer class="site-footer">
    <div class="links">
      <h3>Quick Links</h3>
      <ul>
        <li><a href="#">Home</a></li>
        <li><a href="#">About Us</a></li>
        <li><a href="#">Our Mattresses</a></li>
        <li><a href="#">Contact Us</a></li>
        <li><a href="#">Privacy Policy</a></li>
        <li><a href="#">Terms &amp; Conditions</a></li>
      </ul>
    </div>
    <div class="quick-contact">
      <h3>Quick Contact</h3>
      <span class="field">Name</span>
      <span class="field">Email</span>
      <span class="field">Phone</span>
      <span class="field message">Message</span>
      <span class="submit">SUBMIT</span>
    </div>
    <div class="map" role="img" aria-label="Street map of the store location"></div>
    <div class="follow">
      <h3>Follow Us</h3>
      <ul>
        <li><span class="circle c1"></span>Friendwall</li>
        <li><span class="circle c2"></span>Chirpline</li>
        <li><span class="circle c3"></span>Workmesh</li>
        <li><span class="circle c4"></span>Circleboard</li>
      </ul>
    </div>
  </footer>
  <div class="copyright">Copyright 2024 QR Bedding. All rights reserved.</div>
</div>
</body>
</html>
```